Anesthesia Medical Practice Business Card

We need a business card to hand out to surgeons with my basic information. Something that stands out but is not over the top. The medical community is rather conservative. I'd like them to call me first when flipping through their rolodex of anesthesiologists. I'd like the card to communicate confidence, control, professionalism yet serenity. I don't want the card to be pricey to print.

he logo will be provided as a vector graphic in addition to a complete business card design including the logo

Rex Alba Tovell, M.D.
Board Certified Anesthesiologist

(555) 638-2175

rtovell@quillnet.example

Mailing Address:
48317 Pemberly Ave.
Suite 274-6583
Los Angeles, CA 90871

A logo that inegrates my initials perhaps
RT MD
My initials are RT and MD as in Medical Doctor

or
perhaps a physician in surgical mask and cap caring for a patient

Surgeons who need anesthesia services

Medical

• the logo will be provided as a vector graphic in addition to a complete business card design including the logo

Rex Alba Tovell, M.D.

(555) 638-2175

rtovell@quillnet.example

Mailing Address:
48317 Pemberly Ave.
Suite 274-6583
Los Angeles, CA 90871

• A logo that inegrates my initials perhaps
RT MD

or

```html
<!DOCTYPE html>
<html lang="en">
<head>
<meta charset="utf-8">
<title>Rex Alba Tovell, M.D. — Business Card</title>
<link rel="stylesheet" href="https://fonts.googleapis.com/css2?family=Alegreya:ital,wght@0,400;0,500;1,400&display=swap">
<style>
  :root {
    --ink: #2f2a85;
    --ink-soft: #c9c7e8;
    --paper: #ffffff;
    --backdrop: #e9e8ee;
    --reverse-text: #f2f1fb;
    --mark-fill: #4a45a0;
  }
  * { margin: 0; padding: 0; box-sizing: border-box; }
  html, body {
    width: 1200px;
    height: 873px;
    overflow: hidden;
    background: var(--backdrop);
    font-family: "Alegreya", Georgia, serif;
  }
  .sheet {
    width: 1200px;
    height: 873px;
    display: flex;
    align-items: center;
    justify-content: center;
    gap: 60px;
  }
  .card {
    width: 510px;
    height: 291px;
    border-radius: 3px;
    box-shadow: 0 2px 10px rgba(40, 36, 90, 0.18);
    position: relative;
  }
  .card__name {
    font-size: 25px;
    font-weight: 500;
    letter-spacing: 0.2px;
    line-height: 1.1;
  }
  .card__title {
    font-style: italic;
    font-size: 16px;
    margin-top: 3px;
  }

  /* Contact side */
  .card--front {
    background: var(--paper);
    color: var(--ink);
    padding: 34px 38px;
  }
  .card__rule {
    display: block;
    width: 100%;
    height: 3px;
    margin: 12px 0 16px;
  }
  .card__contact {
    list-style: none;
    font-size: 16px;
    line-height: 1.45;
  }

  /* Brand side */
  .card--back {
    background: var(--ink);
    color: var(--reverse-text);
    padding: 30px 38px;
    display: flex;
    flex-direction: column;
    justify-content: flex-end;
  }
  .card__mark {
    position: absolute;
    top: 28px;
    right: 56px;
    width: 104px;
    height: 104px;
    border-radius: 50%;
    background: var(--mark-fill);
  }
  .card--back .card__name { font-size: 30px; }
  .card--back .card__title { font-size: 19px; font-style: normal; margin-top: 4px; }
</style>
</head>
<body>
<main class="sheet">
  <section class="card card--front" aria-label="Business card, contact side">
    <h1 class="card__name">Rex Alba Tovell, M.D.</h1>
    <p class="card__title">Board Certified Anesthesiologist</p>
    <svg class="card__rule" viewBox="0 0 434 3" preserveAspectRatio="none" aria-hidden="true">
      <defs>
        <linearGradient id="rule-fade" x1="0" x2="1" y1="0" y2="0">
          <stop offset="0" stop-color="#2f2a85"/>
          <stop offset="1" stop-color="#c9c7e8"/>
        </linearGradient>
      </defs>
      <rect width="434" height="3" fill="url(#rule-fade)"/>
    </svg>
    <ul class="card__contact">
      <li>(555) 638-2175</li>
      <li>rtovell@quillnet.example</li>
      <li>48317 Pemberly Ave.</li>
      <li>Suite 274-6583</li>
      <li>Los Angeles, CA 90871</li>
    </ul>
  </section>

  <section class="card card--back" aria-label="Business card, brand side">
    <div class="card__mark" role="img" aria-label="Monogram logo placeholder"></div>
    <h2 class="card__name">Rex Alba Tovell, M.D.</h2>
    <p class="card__title">Board Certified Anesthesiologist</p>
  </section>
</main>
</body>
</html>
```